Postcard Design

Cinder Vale Partners is a waste and Recycling company. We want to purchase recyclable materials from businesses. We would like to use the colors green and grey. The exact colors needed in this project are described below. We would like to have a picture of waste cardboard,a picture of money, and and the line- Are you getting top dollar for your Recyclables? After please put our logo and our phone number: 800.742.5196, our website (bronlomar.com),
and our email address: marisol@bronlomar.com.

* Postcard must contain our logo. Please see buisness card for branding

Industry/Entity Type

It Company

Requirements
Must have
• This postcard must contain the logo and these colors:
Pantone: 576C & 418C

```html
<!DOCTYPE html>
<html lang="en">
<head>
<meta charset="utf-8">
<title>Cinder Vale Partners – Postcard</title>
<link href="https://fonts.googleapis.com/css2?family=Arimo:wght@400;700&display=swap" rel="stylesheet">
<style>
  :root {
    --backdrop: #4d4d4f;
    --paper: #ffffff;
    --brand-green: #5b8a32;
    --brand-grey: #55564d;
    --ink: #1e1e1e;
    --accent-yellow: #f2e600;
    --cardboard-light: #d3a86f;
    --cardboard-dark: #b4834b;
    --money-light: #f1f1e6;
    --money-dark: #c9cdb8;
  }
  * { margin: 0; padding: 0; box-sizing: border-box; }
  html, body {
    width: 958px; height: 1200px; overflow: hidden;
    background: var(--backdrop);
    font-family: "Arimo", "Helvetica Neue", Arial, sans-serif;
  }
  .postcard {
    position: absolute; left: 76px; top: 78px;
    width: 804px; height: 1044px;
    background: var(--paper);
  }
  .photo { position: absolute; }
  .photo-cardboard {
    left: 54px; top: 28px; width: 680px; height: 285px;
    background: linear-gradient(160deg, var(--cardboard-light), var(--cardboard-dark));
    border-radius: 4px;
  }
  .photo-money {
    left: 180px; top: 537px; width: 560px; height: 270px;
    background: linear-gradient(170deg, var(--money-light), var(--money-dark));
    border-radius: 3px;
  }
  .headline { position: absolute; left: 64px; top: 336px; line-height: 1; }
  .headline-lead {
    display: block; font-size: 36px; font-weight: 400;
    color: var(--ink); letter-spacing: 0.2px;
  }
  .headline-row { display: block; margin-top: 14px; white-space: nowrap; }
  .headline-key {
    font-size: 62px; font-weight: 700; color: var(--brand-green);
    letter-spacing: -0.5px;
  }
  .headline-small { font-size: 34px; color: var(--ink); margin-left: 6px; }
  .headline-big {
    display: block; margin-top: 4px;
    font-size: 76px; font-weight: 700; color: var(--brand-green);
    letter-spacing: -0.5px;
  }
  .contact-band {
    position: absolute; left: 0; top: 839px; width: 804px; height: 45px;
    background: var(--brand-green);
    display: flex; align-items: center; gap: 26px; padding-left: 50px;
    color: #fff; font-size: 21px; font-weight: 700;
  }
  .contact-item { display: flex; align-items: center; gap: 6px; }
  .chevron { width: 20px; height: 16px; }
  .contact-person { position: absolute; left: 42px; top: 951px; }
  .contact-label { font-size: 18px; color: var(--ink); }
  .contact-name {
    margin-top: 6px; font-size: 27px; color: var(--brand-green);
    font-weight: 400; letter-spacing: 0.2px;
  }
  .brand { position: absolute; right: 40px; top: 960px; display: flex; align-items: center; gap: 10px; }
  .brand-square { width: 22px; height: 22px; background: var(--brand-green); }
  .brand-name { font-size: 26px; font-weight: 700; color: var(--brand-grey); }
</style>
</head>
<body>
  <main class="postcard">
    <div class="photo photo-cardboard" role="img" aria-label="Stack of flattened waste cardboard boxes"></div>

    <h1 class="headline">
      <span class="headline-lead">ARE YOU GETTING</span>
      <span class="headline-row"><span class="headline-key">TOP DOLLAR</span><span class="headline-small">FOR YOUR</span></span>
      <span class="headline-big">RECYCLABLES?</span>
    </h1>

    <div class="photo photo-money" role="img" aria-label="Fanned stack of hundred dollar bills"></div>

    <div class="contact-band">
      <span class="contact-item">
        <svg class="chevron" viewBox="0 0 20 16"><path d="M1 1l6 7-6 7M10 1l6 7-6 7" fill="none" stroke="var(--accent-yellow)" stroke-width="3"/></svg>
        800.742.5196
      </span>
      <span class="contact-item">
        <svg class="chevron" viewBox="0 0 20 16"><path d="M1 1l6 7-6 7M10 1l6 7-6 7" fill="none" stroke="var(--accent-yellow)" stroke-width="3"/></svg>
        marisol@bronlomar.com.
      </span>
      <span class="contact-item">
        <svg class="chevron" viewBox="0 0 20 16"><path d="M1 1l6 7-6 7M10 1l6 7-6 7" fill="none" stroke="var(--accent-yellow)" stroke-width="3"/></svg>
        www.bronlomar.com
      </span>
    </div>

    <div class="contact-person">
      <p class="contact-label">For More Contact :</p>
      <p class="contact-name">MARISOL QUENBY</p>
    </div>

    <div class="brand">
      <span class="brand-square"></span>
      <span class="brand-name">Cinder Vale Partners</span>
    </div>
  </main>
</body>
</html>
```